Energy trading company (Voltrisa) needs a business card

We need a business card for a company based in Central America. Our main purpose is trading energy . We already have the logo but we need some good creativity to design a high impact business card. Colors blue, orange, green can be used or we would like to see good combinatios with our logo

Target Market(s)

Energy

Industry/Entity Type

Power Generation

Contact Information for Business Card

Logo , headquarters , name, background

Font styles to use
Serif
Sans Serif

Colors

Designer to choose colors to be used in the design.

Requirements
Must have
• it must have a fresh and clean view
Nice to have
• good backgrounds that combine with the logo
Should not have
• too much words

```html
<!DOCTYPE html>
<html lang="en">
<head>
<meta charset="utf-8">
<title>Voltrisa Business Card</title>
<link href="https://fonts.googleapis.com/css2?family=Mulish:wght@500&family=Arimo:wght@400;700&display=swap" rel="stylesheet">
<style>
  :root {
    --stage: #1e1e1e;
    --card: #ffffff;
    --brand-orange: #f7931e;
    --ink: #3a3a3a;
  }
  * { margin: 0; padding: 0; box-sizing: border-box; }
  html, body { width: 1200px; height: 900px; overflow: hidden; }
  body {
    background: var(--stage);
    display: flex;
    flex-direction: column;
    align-items: center;
    justify-content: center;
    gap: 36px;
    font-family: "Arimo", Arial, sans-serif;
  }
  .card {
    width: 700px;
    height: 400px;
    background: var(--card);
    position: relative;
    box-shadow: 0 10px 30px rgba(0,0,0,0.5);
  }
  .brand {
    display: flex;
    flex-direction: column;
    align-items: center;
    color: var(--brand-orange);
  }
  .brand-dot {
    border-radius: 50%;
    background: var(--brand-orange);
  }
  .brand-name {
    font-family: "Mulish", "Avenir", sans-serif;
    font-weight: 500;
    letter-spacing: 0.02em;
    line-height: 1;
  }
  /* front */
  .card-front { display: flex; align-items: center; justify-content: center; }
  .card-front .brand-dot { width: 96px; height: 96px; margin-bottom: 18px; }
  .card-front .brand-name { font-size: 84px; }
  /* back */
  .card-back .brand { position: absolute; top: 48px; left: 0; right: 0; }
  .card-back .brand-dot { width: 64px; height: 64px; margin-bottom: 12px; }
  .card-back .brand-name { font-size: 56px; }
  .details {
    position: absolute;
    top: 222px;
    left: 0; right: 0;
    display: flex;
    justify-content: center;
  }
  .person {
    text-align: right;
    padding-right: 22px;
    border-right: 2px solid var(--brand-orange);
    width: 270px;
  }
  .person-name {
    font-weight: 700;
    font-size: 26px;
    letter-spacing: 0.04em;
    color: var(--brand-orange);
  }
  .person-role { font-size: 17px; color: var(--ink); margin-top: 2px; }
  .contact-list {
    list-style: none;
    padding-left: 22px;
    width: 270px;
    font-size: 17px;
    color: var(--ink);
  }
  .contact-list li { display: flex; align-items: center; gap: 10px; line-height: 26px; }
  .contact-list svg { width: 16px; height: 16px; flex: none; }
  .address {
    position: absolute;
    bottom: 40px;
    left: 0; right: 0;
    text-align: center;
    font-size: 17px;
    color: var(--ink);
  }
</style>
</head>
<body>
  <section class="card card-front">
    <div class="brand">
      <span class="brand-dot"></span>
      <span class="brand-name">VOLTRISA</span>
    </div>
  </section>

  <section class="card card-back">
    <div class="brand">
      <span class="brand-dot"></span>
      <span class="brand-name">VOLTRISA</span>
    </div>
    <div class="details">
      <div class="person">
        <div class="person-name">DANIEL REYES</div>
        <div class="person-role">President</div>
      </div>
      <ul class="contact-list">
        <li>
          <svg viewBox="0 0 16 16" aria-hidden="true"><path d="M3 1.5l2.5 0 1.2 3-1.6 1.2a8 8 0 0 0 5.2 5.2l1.2-1.6 3 1.2 0 2.5a1.5 1.5 0 0 1-1.6 1.5A13 13 0 0 1 1.5 3.1 1.5 1.5 0 0 1 3 1.5z" fill="#f7931e"/></svg>
          +00 000 000 000
        </li>
        <li>
          <svg viewBox="0 0 16 16" aria-hidden="true"><rect x="1" y="3" width="14" height="10" fill="none" stroke="#f7931e" stroke-width="1.3"/><path d="M1 3l7 6 7-6" fill="none" stroke="#f7931e" stroke-width="1.3"/></svg>
          info@voltrisa.com
        </li>
        <li>
          <svg viewBox="0 0 16 16" aria-hidden="true"><g fill="none" stroke="#f7931e" stroke-width="1.2"><circle cx="8" cy="8" r="6.5"/><ellipse cx="8" cy="8" rx="3" ry="6.5"/><path d="M1.5 8h13M2.5 4.5h11M2.5 11.5h11"/></g></svg>
          www.voltrisa.com
        </li>
      </ul>
    </div>
    <p class="address">00000 1st Ave S Ste 201, Central America, WA 00000</p>
  </section>
</body>
</html>
```